Letterhead and Envelope for Mental Health Business

I need letterhead and envelope designs that will match my business cards. I am attaching a *.pds file of my business card so it can be matched.

```html
<!DOCTYPE html>
<html lang="en">
<head>
<meta charset="utf-8">
<title>Alder Counseling — Letterhead</title>
<link rel="stylesheet" href="https://fonts.googleapis.com/css2?family=Arimo:wght@400&display=swap">
<style>
  :root {
    --paper: #ffffff;
    --brand-blue: #2b5a9a;
    --brand-green: #5a9a3a;
    --text-blue: #2c4f86;
    --mark-grey: #e8e8e8;
    --font-text: "Arimo", Arial, sans-serif;
  }
  * { margin: 0; padding: 0; box-sizing: border-box; }
  html, body {
    width: 1200px;
    height: 900px;
    overflow: hidden;
    background: var(--paper);
  }
  .letterhead {
    position: relative;
    width: 1200px;
    height: 900px;
    background: var(--paper);
    font-family: var(--font-text);
  }
  .brand {
    position: absolute;
    left: 108px;
    top: 56px;
    display: flex;
    align-items: center;
    gap: 14px;
  }
  .brand-dot {
    width: 54px;
    height: 54px;
    border-radius: 50%;
    background: var(--brand-blue);
  }
  .brand-name {
    font-family: var(--font-text);
    font-weight: 400;
    font-size: 30px;
    letter-spacing: 2px;
    color: var(--brand-blue);
    line-height: 1;
  }
  .backdrop-mark {
    position: absolute;
    left: 220px;
    top: 238px;
    width: 740px;
    height: 390px;
  }
  .footer {
    position: absolute;
    left: 96px;
    right: 95px;
    top: 812px;
    display: flex;
    justify-content: space-between;
    align-items: center;
    color: var(--text-blue);
    font-size: 13.5px;
    letter-spacing: 4.2px;
    line-height: 21px;
  }
  .footer-contact { text-align: left; }
  .footer-location { text-align: right; }
  .footer-dot {
    position: absolute;
    left: 474px;
    top: -4px;
    width: 70px;
    height: 40px;
    border-radius: 50%;
    border: 5px solid var(--brand-blue);
  }
</style>
</head>
<body>
  <main class="letterhead">
    <header class="brand">
      <span class="brand-dot" aria-hidden="true"></span>
      <span class="brand-name">ALDER COUNSELING</span>
    </header>

    <svg class="backdrop-mark" viewBox="0 0 740 390" aria-hidden="true">
      <ellipse cx="370" cy="195" rx="358" ry="185" fill="none" stroke="var(--mark-grey)" stroke-width="22"/>
    </svg>

    <footer class="footer">
      <div class="footer-contact">
        <div>hello@aldercounselingllc.com</div>
        <div>www.aldercounselingllc.com</div>
      </div>
      <span class="footer-dot" aria-hidden="true"></span>
      <div class="footer-location">
        <div>Elm Street 48, 1020 NY, USA</div>
        <div>555/014-2290</div>
      </div>
    </footer>
  </main>
</body>
</html>
```